Brantwell College Course Brochure

Brantwell College is a private institution providing different courses for students internationally.
We need a series of brochures for 5 new courses individually.(5 pieces in total)
We have opened 5 courses
1. Higher Diploma in Construction & Civil engineering
2.Higher Diploma in Quantity Surveying
3.Higher Diploma in Mechanical Engineering
4.Higher Diploma in Electrical & Electronic Engineering
5.Higher Diploma in Facilities Management

Please give out the design sample using one of the course, then drag and adjust accordingly for other courses

Requirement
*Vibrant and energetic looking
*Size A5 double sided/A4 size double fold
*Please include the given company logo and Learnsafe image
*Refer to "Higher Diploma synopsis" file for course description
*information must be clear to see
*Entry requirements modules and other course details must be included in
*Redesign according to the attached files
* a PSD file is attached for reference and obtain information

Target Market(s)

International students above 21 years old

Industry/Entity Type

Education

Font styles to use
Sans Serif

Requirements
Must have
• *Please include the given company logo and Learnsafe image
• *Summarise the descriptions, do not be wordy.
• *information must be clear to see
• *Entry requirements modules and other course details must be included in
• *attached file for reference
Nice to have
• More catchy images and designs
• Keep it simple
• It is on designer's choice of color, does not have to use only company colours.

```html
<!DOCTYPE html>
<html lang="en">
<head>
<meta charset="utf-8">
<title>Brantwell College – Higher Diploma in Construction &amp; Civil Engineering</title>
<link href="https://fonts.googleapis.com/css2?family=Merriweather:wght@700;900&family=Gelasio:wght@400;700&family=Raleway:wght@500;700&display=swap" rel="stylesheet">
<style>
  :root{
    --stage:#3b3b3d;
    --paper:#ffffff;
    --red:#b3191f;
    --red-dark:#9e1419;
    --orange:#f39322;
    --navy:#1f2566;
    --ink:#333333;
    --rule:#8a8a8a;
  }
  *{margin:0;padding:0;box-sizing:border-box}
  html,body{width:1200px;height:960px;overflow:hidden;background:var(--stage)}
  .canvas{position:relative;width:1200px;height:960px}

  .page{position:absolute;background:var(--paper);overflow:hidden;box-shadow:0 6px 18px rgba(0,0,0,.45)}
  .page--front{left:36px;top:29px;width:554px;height:785px}
  .page--inside{left:638px;top:198px;width:520px;height:739px}

  .front-art{position:absolute;inset:0}

  .brand{position:absolute;left:40px;top:70px;width:150px;text-align:center;display:flex;flex-direction:column;align-items:center;gap:8px}
  .brand__dot{width:56px;height:56px;border-radius:50%;background:var(--navy)}
  .brand__name{font-family:"Gelasio",serif;font-weight:700;font-size:14px;color:var(--navy);letter-spacing:.2px}

  .course-title{position:absolute;left:19px;top:282px;font-family:"Merriweather",serif;font-weight:900;font-size:27px;line-height:39.5px;color:#fff}

  .intro{position:absolute;left:18px;top:458px;width:315px;font-family:"Gelasio",serif;font-size:14.6px;line-height:17.4px;color:var(--ink);text-align:justify}
  .intro p+p{margin-top:17px}

  .contact{position:absolute;left:402px;top:589px;width:150px;font-family:"Raleway",sans-serif;font-size:8.6px;line-height:12.4px;color:#fff}
  .contact__title{font-weight:700;font-size:10.2px;margin-bottom:2px}
  .contact__row{display:flex;gap:5px;align-items:flex-start}
  .contact__row svg{flex:none;margin-top:1px}
  .contact__indent{padding-left:26px}
  .follow{position:absolute;left:409px;top:733px;display:flex;align-items:center;gap:6px;font-family:"Raleway",sans-serif;font-weight:700;font-size:10px;color:#fff}
  .follow__box{width:13px;height:13px;background:#3b5998}

  .badge{position:absolute;left:284px;top:732px;display:flex;flex-direction:column;align-items:flex-start}
  .badge__row{display:flex;align-items:center;gap:4px}
  .badge__dot{width:28px;height:28px;border-radius:50%;background:var(--red)}
  .badge__name{font-family:"Gelasio",serif;font-size:17px;color:var(--ink)}
  .badge__cert{font-family:"Raleway",sans-serif;font-size:4px;color:#555;margin-top:2px}

  .inside-art{position:absolute;left:0;top:0}

  .criteria{position:absolute;font-family:"Gelasio",serif;font-size:9.3px;line-height:12px;color:#222}
  .criteria h3{font-size:10.4px;font-weight:700;color:var(--navy);line-height:12px}
  .criteria h4{font-size:10.4px;font-weight:700;color:var(--orange);line-height:12px}
  .criteria p{text-align:justify}
  .criteria .gap{margin-top:12px}
  .criteria--diploma{left:294px;top:237px;width:215px}
  .criteria--higher{left:294px;top:344px;width:215px}
  .criteria--language{left:294px;top:433px;width:215px}
  .criteria--relevant{left:21px;top:355px;width:250px}
  .criteria--working{left:21px;top:438px;width:250px}

  .modules{position:absolute;left:15px;top:498px;width:491px;border-collapse:collapse;font-family:"Gelasio",serif;font-size:10.8px;color:#111}
  .modules td,.modules th{height:16px;padding:0 2px;border:1px solid var(--rule);font-weight:400;text-align:left;white-space:nowrap;line-height:14px}
  .modules col.c-code{width:74px}
  .modules col.c-mod{width:269px}
  .modules col.c-cred{width:48px}
  .modules col.c-assess{width:100px}
  .modules thead tr.head th{background:var(--red-dark);color:#fff}
  .modules thead tr.programme th{background:var(--orange);color:#fff}
  .modules .num{text-align:center}
  .modules .exam{color:#e0262c}
  .modules tbody td{border-left:none;border-right:none}
  .modules tbody td+td{border-left:1px solid var(--rule)}
</style>
</head>
<body>
<div class="canvas">

  <!-- Front cover -->
  <section class="page page--front">
    <svg class="front-art" width="554" height="785" viewBox="0 0 554 785">
      <defs>
        <linearGradient id="site" x1="0" y1="0" x2="1" y2="1">
          <stop offset="0" stop-color="#d9d4cc"/>
          <stop offset=".5" stop-color="#a79c8e"/>
          <stop offset="1" stop-color="#7d7268"/>
        </linearGradient>
        <linearGradient id="yard" x1="0" y1="0" x2="1" y2="0">
          <stop offset="0" stop-color="#8c9aa6"/>
          <stop offset="1" stop-color="#c7d0d8"/>
        </linearGradient>
        <linearGradient id="band" x1="0" y1="0" x2="0" y2="1">
          <stop offset="0" stop-color="#c21e24"/>
          <stop offset="1" stop-color="#a5161b"/>
        </linearGradient>
      </defs>
      <polygon role="img" aria-label="Photo of a young engineer in an orange hard hat holding a clipboard in front of high-rise buildings under construction" points="170,0 554,0 554,343 354,435 0,435 0,193 240,193" fill="url(#site)"/>
      <polygon role="img" aria-label="Photo of a busy construction yard with cranes and scaffolding" points="354,435 554,343 554,443 386,515" fill="url(#yard)"/>
      <polygon points="0,193 240,193 344,433 0,433" fill="url(#band)"/>
      <polygon points="386,515 554,443 554,785 386,785" fill="var(--orange)"/>
    </svg>

    <div class="brand">
      <span class="brand__dot"></span>
      <span class="brand__name">BRANTWELL COLLEGE</span>
    </div>

    <h1 class="course-title">Higher Diploma in<br>Construction &amp;<br>Civil Engineering</h1>

    <div class="intro">
      <p>The Higher Diploma in Construction &amp; Civil Engineering is a broad-based course that provides students with in-depth knowledge in civil engineering within the context of a construction environment. The module will cover theories and concepts of construction &amp; civil engineering.</p>
      <p>The curriculum will include recent innovate skills for engaging the more challenging and complex needs in the industry. A focus on working in groups and classroom communication and collaboration are essential to prepare students for the future. In this course, you will acquire these skills through industry based projects, case studies and assignments.</p>
    </div>

    <div class="badge">
      <div class="badge__row"><span class="badge__dot"></span><span class="badge__name">Learnsafe</span></div>
      <span class="badge__cert">Cert No. EDU-0-0000 Validity: 2024 - 2028</span>
    </div>

    <div class="contact">
      <div class="contact__title">Contact Us</div>
      <div>www.brantwellcollege.edu.sg</div>
      <div class="contact__row">
        <svg width="12" height="14" viewBox="0 0 12 14"><path d="M3 1 L5 4 L3.8 5.6 Q5 8.6 7.6 10.2 L9 9 L11.5 11 L10 13 Q4 12 1.5 3 Z" fill="#fff"/></svg>
        <div style="padding-left:9px">+65 6100 2480<br>+65 9200 7316</div>
      </div>
      <div class="contact__row">
        <svg width="12" height="11" viewBox="0 0 12 11"><rect x="3" y="0" width="6" height="3" fill="#fff"/><rect x="0" y="3.5" width="12" height="5" fill="#fff"/><rect x="3" y="7" width="6" height="4" fill="#fff" stroke="var(--orange)" stroke-width=".6"/></svg>
        <div style="padding-left:9px">+65 6100 2481</div>
      </div>
      <div class="contact__row">
        <svg width="12" height="9" viewBox="0 0 12 9"><rect x=".5" y=".5" width="11" height="8" fill="#fff"/><path d="M.5 .5 L6 5 L11.5 .5" fill="none" stroke="var(--orange)" stroke-width="1"/></svg>
        <div>info@brantwellcollege.edu.sg</div>
      </div>
      <div class="contact__row" style="margin-left:-15px">
        <svg width="11" height="11" viewBox="0 0 11 11"><path d="M5.5 0 L11 5 L9.5 5 L9.5 11 L6.5 11 L6.5 7.5 L4.5 7.5 L4.5 11 L1.5 11 L1.5 5 L0 5 Z" fill="#fff"/></svg>
        <div>admissions@brantwellcollege.edu.sg</div>
      </div>
      <div>48, Harbourline Road #03-12<br>Tower 2, Meridian Point,<br>Singapore 100482</div>
    </div>

    <div class="follow">Follow Us On <span class="follow__box"></span></div>
  </section>

  <!-- Inside page -->
  <section class="page page--inside">
    <svg class="inside-art" width="520" height="340" viewBox="0 0 520 340">
      <defs>
        <linearGradient id="dusk" x1="0" y1="0" x2="0" y2="1">
          <stop offset="0" stop-color="#6e5a2c"/>
          <stop offset=".55" stop-color="#a47a2a"/>
          <stop offset="1" stop-color="#5a2a1c"/>
        </linearGradient>
        <linearGradient id="plans" x1="0" y1="0" x2="1" y2="1">
          <stop offset="0" stop-color="#8c9096"/>
          <stop offset="1" stop-color="#4a4f57"/>
        </linearGradient>
      </defs>
      <g role="img" aria-label="Photo of tower cranes over a building frame at dusk, beside construction plans and a calculator">
        <polygon points="0,0 452,0 259,218 160,330 0,190" fill="url(#dusk)"/>
        <polygon points="452,0 520,0 520,218 259,218" fill="url(#plans)"/>
        <polygon points="160,330 290,0 452,0" fill="#b3191f" opacity=".85"/>
      </g>
    </svg>

    <div class="criteria criteria--diploma">
      <h3>Diploma Admission Criteria</h3>
      <p>The minimum entry requirements for the course are:</p>
      <p class="gap">Age 18 years and above<br>Minimum GCE 'O' Level with 3-subject passes or equivalent.<br>IELTS 5.5 or equivalent.</p>
    </div>

    <div class="criteria criteria--higher">
      <h3>Higher Diploma&nbsp; Admission Criteria</h3>
      <h4>Academic Level</h4>
      <p>'A' Level 3 subjects passes. English plus any other subjects or; a related Diploma from local Polytechnic or; other CPE registered PEI or equivalent (Diplomas from other countries)<br>Minimum 21 years and above.</p>
    </div>

    <div class="criteria criteria--language">
      <h3>Language Proficiency</h3>
      <p>IELTS 5.5 or equivalent</p>
    </div>

    <div class="criteria criteria--relevant">
      <h3>Relevant Working Experience</h3>
      <p>Student with other diploma qualifications with minimum age of 23 years with at least 3 years working experience in relevant field. Recognition of Prior Learning (RPL) will be done to analysis whether student has met the required skills to be admitted onto our Higher Diplomas.</p>
    </div>

    <div class="criteria criteria--working">
      <h3>Working Experience</h3>
      <p>Matured students, of 30 years old with at least 8 years of working experience will be considered on an individual basis.</p>
    </div>

    <table class="modules">
      <colgroup><col class="c-code"><col class="c-mod"><col class="c-cred"><col class="c-assess"></colgroup>
      <thead>
        <tr class="head"><th>Code</th><th>Modules</th><th class="num">Credits</th><th class="num">Assessment</th></tr>
        <tr class="programme"><th>HDCCE</th><th>Higher Diploma in Construction &amp; Civil Engineering</th><th class="num">Credits</th><th></th></tr>
      </thead>
      <tbody>
        <tr><td>CCET201</td><td>Construction &amp; Civil Engineering Technology 1</td><td class="num">20</td><td>100% coursework</td></tr>
        <tr><td>EM202</td><td>Engineering Mathematics</td><td class="num">20</td><td class="exam">100% Examination</td></tr>
        <tr><td>SM203</td><td>Science of Materials</td><td class="num">20</td><td>100% coursework</td></tr>
        <tr><td>WSH204</td><td>Workplace Safety and Health Practice</td><td class="num">20</td><td>100% coursework</td></tr>
        <tr><td>GEDA205</td><td>Green Engineering Design and Application</td><td class="num">20</td><td>100% coursework</td></tr>
        <tr><td>PC206</td><td>Professions in Context</td><td class="num">20</td><td>100% coursework</td></tr>
        <tr><td>CCET301</td><td>Construction &amp; Civil Engineering Technology 2</td><td class="num">20</td><td>100% coursework</td></tr>
        <tr><td>AEM302</td><td>Advanced Engineering Mathematics</td><td class="num">20</td><td class="exam">100% Examination</td></tr>
        <tr><td>SAD303</td><td>Structural Analysis and Design</td><td class="num">20</td><td>100% coursework</td></tr>
        <tr><td>OM304</td><td>Operations Management</td><td class="num">20</td><td>100% coursework</td></tr>
        <tr><td>EGSM305</td><td>Engineering Geology and Soil Mechanics</td><td class="num">20</td><td>100% coursework</td></tr>
        <tr><td>PPP306</td><td>Professional Practice Project</td><td class="num">20</td><td>100% coursework</td></tr>
      </tbody>
    </table>
  </section>

</div>
</body>
</html>
```